Stationary/business card/envelope design for Larkvale Dentalcare

We are located in the foothills of the sierra nevada mountains. We are looking for a beautiful classy modern stationary. We need evelopes and business card design all to flow seamlessly. Envelope design.

Additional office address 4816 Meridian Wy., Suite B, Auburn, CA 95604 Phone: pending Fax: pending.

3 different Drs on each business card:
Helen R. Marsh, DDS
Orla P. Marsh, DDS
Rebecca S. Halvey, DDS

Target Market(s)

Dental patients

Industry/Entity Type

Dental

Contact Information for Business Card

Two sided. See example.

Font styles to use
Sans Serif

Requirements
Must have
• One sided business cards. Need envelope design.
Colors should match existing logo.

Helen R. Marsh, DDS
Orla P. Marsh, DDS
Rebecca S. Halvey, DDS

```html
<!DOCTYPE html>
<html lang="en">
<head>
<meta charset="utf-8">
<title>Larkvale Dentalcare Stationery</title>
<link href="https://fonts.googleapis.com/css2?family=Open+Sans:wght@400;600;700&display=swap" rel="stylesheet">
<style>
:root{
  --green:#2f7a3b;
  --blue:#38ace2;
  --ink:#4a4a4a;
  --pine:#cdd9ca;
  --paper:#ffffff;
  --backdrop:#e9e6e1;
  --rule:#8a8a8a;
}
*{margin:0;padding:0;box-sizing:border-box}
html,body{width:1200px;height:1200px;overflow:hidden}
body{background:var(--backdrop);font-family:"Open Sans",sans-serif;color:var(--ink);position:relative}
.sheet{position:absolute;background:var(--paper);overflow:hidden;box-shadow:0 2px 8px rgba(0,0,0,.15)}
.pine-art{position:absolute;background:linear-gradient(180deg,rgba(205,217,202,0) 0%,var(--pine) 35%,var(--pine) 100%)}
.brand{position:absolute;display:flex;align-items:center;gap:5px}
.brand-dot{border-radius:50%;background:var(--blue);flex:none}
.brand-name{color:var(--green);font-weight:600;white-space:nowrap}
.ico{width:7px;height:7px;fill:var(--blue);display:inline-block;vertical-align:-1px;margin-right:2px}
.line{position:absolute;white-space:nowrap}

/* business card */
.card{left:233px;top:121px;width:316px;height:181px}
.card .pine-art{right:0;top:4px;width:80px;height:177px}
.card .name{left:14px;top:83px;font-size:10px;font-weight:700;color:var(--green)}
.card .title{left:14px;top:96px;font-size:7px}
.card .small{font-size:7px}
.card .divider{position:absolute;left:14px;right:40px;top:160px;height:1px;background:var(--rule)}

/* appointment card */
.appt{left:650px;top:121px;width:317px;height:181px}
.appt .pine-art{right:0;top:4px;width:80px;height:177px}
.appt .heading{left:0;width:317px;top:13px;text-align:center;font-size:8.5px;font-weight:600;color:var(--blue)}
.appt .row{left:96px;font-size:8.5px;color:var(--green)}
.appt .blank{display:inline-block;border-bottom:1px solid var(--green);vertical-align:baseline}
.appt .notice{left:0;width:317px;text-align:center;top:142px;font-size:8px;color:var(--green)}
.appt .web{left:0;width:317px;text-align:center;top:156px;font-size:7.5px;letter-spacing:.8px}

/* envelopes */
.env-front{left:54px;top:492px;width:543px;height:237px}
.env-front .pine-art{right:0;top:14px;width:100px;height:223px}
.env-back{left:54px;top:787px;width:543px;height:237px}
.env-back svg{position:absolute;left:0;top:0}

/* letterhead */
.letter{left:630px;top:437px;width:510px;height:660px}
.letter .pine-art{right:0;top:103px;width:260px;height:557px}
.letter .foot{font-size:7px;left:0;width:510px;text-align:center}
.letter .divider{position:absolute;left:50px;right:50px;top:628px;height:1px;background:var(--rule)}
</style>
</head>
<body>

<!-- Business card -->
<section class="sheet card">
  <div class="pine-art" role="img" aria-label="Faint pale-green pine tree silhouette"></div>
  <div class="brand" style="left:14px;top:30px">
    <span class="brand-dot" style="width:16px;height:16px"></span>
    <span class="brand-name" style="font-size:9px">Larkvale Dentalcare</span>
  </div>
  <div class="line name">Helen R. Marsh, DDS</div>
  <div class="line title">Family &amp; Cosmetic Dentistry</div>
  <div class="line small" style="left:14px;top:117px">
    <svg class="ico" viewBox="0 0 10 10"><path d="M2 0h2l1 3-1.5 1a6 6 0 0 0 2.5 2.5L7 5l3 1v2a2 2 0 0 1-2 2A8 8 0 0 1 0 2a2 2 0 0 1 2-2z"/></svg>(916) 555-0142
    &nbsp;<svg class="ico" viewBox="0 0 10 10"><rect x="1" y="4" width="8" height="5"/><rect x="3" y="0" width="4" height="4"/></svg>(916) 555-0187
  </div>
  <div class="line small" style="left:14px;top:137px;line-height:10px">
    <svg class="ico" viewBox="0 0 10 10"><path d="M5 0a3.5 3.5 0 0 1 3.5 3.5C8.5 6 5 10 5 10S1.5 6 1.5 3.5A3.5 3.5 0 0 1 5 0z"/></svg>2291 Ridgecrest Road<br>&nbsp;&nbsp;&nbsp;Folsom, California 95631
  </div>
  <div class="line small" style="left:125px;top:136px;line-height:10px">
    <svg class="ico" viewBox="0 0 10 10"><path d="M5 0a3.5 3.5 0 0 1 3.5 3.5C8.5 6 5 10 5 10S1.5 6 1.5 3.5A3.5 3.5 0 0 1 5 0z"/></svg>office 4816 Meridian Wy.<br>&nbsp;&nbsp;&nbsp;Suite B, Auburn, CA 95604
  </div>
  <div class="divider"></div>
  <div class="line small" style="left:14px;top:161px">
    <svg class="ico" viewBox="0 0 10 10"><path d="M0 2h10v6H0z"/></svg>larkvaledentalcare@mail.com
    &nbsp;&nbsp;<svg class="ico" viewBox="0 0 10 10"><circle cx="5" cy="5" r="5"/></svg>www.larkvaledentalcare.com
  </div>
</section>

<!-- Appointment card -->
<section class="sheet appt">
  <div class="pine-art" role="img" aria-label="Faint pale-green pine tree silhouette"></div>
  <div class="line heading">Your Next Appointment</div>
  <div class="line row" style="top:40px">Mon <span class="blank" style="width:70px"></span>at<span class="blank" style="width:26px"></span></div>
  <div class="line row" style="top:58px">Tues <span class="blank" style="width:66px"></span>at<span class="blank" style="width:26px"></span></div>
  <div class="line row" style="top:77px">Wed <span class="blank" style="width:70px"></span>at<span class="blank" style="width:26px"></span></div>
  <div class="line row" style="top:95px">Thu <span class="blank" style="width:73px"></span>at<span class="blank" style="width:26px"></span></div>
  <div class="line row" style="top:114px">Fri <span class="blank" style="width:76px"></span>at<span class="blank" style="width:26px"></span></div>
  <div class="line notice">If Unable To Keep Appointment Kindly Give 24 Hour Notice</div>
  <div class="line web">www.larkvaledentalcare.com</div>
</section>

<!-- Envelope front -->
<section class="sheet env-front">
  <div class="pine-art" role="img" aria-label="Faint pale-green pine tree silhouette"></div>
  <div class="brand" style="left:17px;top:36px">
    <span class="brand-dot" style="width:16px;height:16px"></span>
    <span class="brand-name" style="font-size:9px">Larkvale Dentalcare</span>
  </div>
  <div class="line" style="left:17px;top:82px;font-size:7px;line-height:10px">
    <svg class="ico" viewBox="0 0 10 10"><path d="M5 0a3.5 3.5 0 0 1 3.5 3.5C8.5 6 5 10 5 10S1.5 6 1.5 3.5A3.5 3.5 0 0 1 5 0z"/></svg>2291 Ridgecrest Road<br>&nbsp;&nbsp;&nbsp;Folsom, California 95631
  </div>
</section>

<!-- Envelope back -->
<section class="sheet env-back">
  <svg width="543" height="237" viewBox="0 0 543 237">
    <path d="M0 0H543L528 40Q522 50 505 52L285 86Q272 88 259 86L38 52Q22 50 16 40Z" fill="var(--blue)" stroke="#222" stroke-width="1"/>
  </svg>
</section>

<!-- Letterhead -->
<section class="sheet letter">
  <div class="pine-art" role="img" aria-label="Faint pale-green pine tree silhouette"></div>
  <div class="brand" style="left:26px;top:60px">
    <span class="brand-dot" style="width:24px;height:24px"></span>
    <span class="brand-name" style="font-size:13px">Larkvale Dentalcare</span>
  </div>
  <div class="line foot" style="top:594px">
    <svg class="ico" viewBox="0 0 10 10"><path d="M2 0h2l1 3-1.5 1a6 6 0 0 0 2.5 2.5L7 5l3 1v2a2 2 0 0 1-2 2A8 8 0 0 1 0 2a2 2 0 0 1 2-2z"/></svg>(916) 555-0142
    &nbsp;&nbsp;<svg class="ico" viewBox="0 0 10 10"><rect x="1" y="4" width="8" height="5"/><rect x="3" y="0" width="4" height="4"/></svg>(916) 555-0187
  </div>
  <div class="line foot" style="top:609px">
    <svg class="ico" viewBox="0 0 10 10"><path d="M0 2h10v6H0z"/></svg>larkvaledentalcare@mail.com
    &nbsp;&nbsp;<svg class="ico" viewBox="0 0 10 10"><circle cx="5" cy="5" r="5"/></svg>www.larkvaledentalcare.com
  </div>
  <div class="divider"></div>
  <div class="line foot" style="top:633px">
    <svg class="ico" viewBox="0 0 10 10"><path d="M5 0a3.5 3.5 0 0 1 3.5 3.5C8.5 6 5 10 5 10S1.5 6 1.5 3.5A3.5 3.5 0 0 1 5 0z"/></svg>2291 Ridgecrest Road, Folsom, California 95631
    &nbsp;&nbsp;<svg class="ico" viewBox="0 0 10 10"><path d="M5 0a3.5 3.5 0 0 1 3.5 3.5C8.5 6 5 10 5 10S1.5 6 1.5 3.5A3.5 3.5 0 0 1 5 0z"/></svg>office 4816 Meridian Wy. Suite B, Auburn, CA 95604
  </div>
</section>

</body>
</html>
```